Biz Card for Harrowfield Property Partners - HWPP

Harrowfield Property Partners is a commercial real estate acquisitions firm. We buy commercial property and need to raise capital from investors for each deal we buy. The vibe needs to be: give us your money, we will multiply it.
Our website: www.hrwpp-example.com
Competitors are: https://velmarholdings-example.com/, https://tribanquepartners-example.com/, http://www.ostrellecapital-example.com/
Target Market(s)
High Net Worth Individuals, Bankers, Insurance Companies, Commercial Real Estate Brokers.
Industry/Entity Type
Investment Banking
Contact Information for Business Card
Name, Title, Addess, Cell#, Office#, email, website
Requirements
Must have
- use one of our logos. See website for look and feel: www.hrwpp-example.com
Nice to have
- see website: www.hrwpp-example.com

```html
<!DOCTYPE html>
<html lang="en">
<head>
<meta charset="utf-8">
<title>Harrowfield Property Partners – Business Cards</title>
<link href="https://fonts.googleapis.com/css2?family=Lato:wght@400&family=Montserrat:wght@400;500;600&display=swap" rel="stylesheet">
<style>
  :root {
    --navy: #13273f;
    --white: #ffffff;
    --backdrop: #d8dfe1;
    --ink: #111111;
    --photo-dark: #5f6f7e;
    --photo-mid: #a3afba;
    --photo-light: #e6eaee;
  }
  * { margin: 0; padding: 0; box-sizing: border-box; }
  html, body { width: 1200px; height: 846px; overflow: hidden; }
  body { background: var(--backdrop); position: relative; font-family: "Montserrat", sans-serif; color: var(--ink); }

  .card { position: absolute; width: 507px; height: 290px; overflow: hidden; border: 1px solid #222; background: var(--white); }
  .card--front-dark { left: 17px; top: 29px; background: var(--navy); }
  .card--back-right { left: 67px; top: 319px; }
  .card--front-light { left: 613px; top: 241px; }
  .card--back-left { left: 666px; top: 531px; }

  .card__shape { position: absolute; inset: 0; width: 100%; height: 100%; }

  .brand__mark { position: absolute; left: 214px; top: 55px; width: 78px; height: 78px; border-radius: 50%; }
  .brand__name { position: absolute; left: 0; right: 0; top: 142px; text-align: center; font-family: "Lato", sans-serif; font-weight: 400; font-size: 30px; letter-spacing: 4px; }
  .brand__sub { position: absolute; left: 0; right: 0; top: 178px; text-align: center; font-family: "Lato", sans-serif; font-weight: 400; font-size: 12px; letter-spacing: 2.5px; }
  .brand__web { position: absolute; left: 0; right: 0; top: 213px; text-align: center; font-family: "Montserrat", sans-serif; font-weight: 600; font-size: 16px; letter-spacing: 4.5px; }

  .card--front-dark .brand__mark { background: var(--white); }
  .card--front-dark .brand__name, .card--front-dark .brand__sub, .card--front-dark .brand__web { color: var(--white); }
  .card--front-light .brand__mark { background: var(--navy); }
  .card--front-light .brand__name, .card--front-light .brand__sub, .card--front-light .brand__web { color: var(--navy); }

  .photo { position: absolute; top: 0; }
  .card--back-right .photo { left: 0; width: 380px; height: 100%;
    background: linear-gradient(90deg, var(--photo-dark) 0%, var(--photo-mid) 40%, var(--photo-light) 72%, rgba(255,255,255,0) 100%); }
  .card--back-left .photo { right: 0; width: 420px; height: 245px;
    background: linear-gradient(270deg, var(--photo-dark) 0%, var(--photo-mid) 35%, var(--photo-light) 70%, rgba(255,255,255,0) 100%); }

  .mini-brand { position: absolute; display: flex; align-items: center; gap: 6px; font-family: "Lato", sans-serif; font-weight: 400; }
  .mini-brand__mark { width: 31px; height: 31px; border-radius: 50%; flex: none; }
  .mini-brand__name { font-size: 9.5px; letter-spacing: 1.4px; line-height: 1.25; }
  .card--back-right .mini-brand { right: 30px; top: 26px; color: var(--navy); }
  .card--back-right .mini-brand__mark { background: var(--navy); }
  .card--back-left .mini-brand { left: 10px; top: 254px; color: var(--white); }
  .card--back-left .mini-brand__mark { background: var(--white); }

  .contact__name { position: absolute; font-weight: 600; font-size: 16px; }
  .contact__title { position: absolute; font-weight: 400; font-size: 9.5px; letter-spacing: 0.3px; }
  .contact__rule { position: absolute; height: 2px; background: var(--navy); }
  .contact__line { position: absolute; font-weight: 400; font-size: 12px; }
  .contact__email { font-weight: 600; }
  .contact__office { position: absolute; font-weight: 600; font-size: 12px; }
  .contact__address { position: absolute; font-weight: 400; font-size: 9.5px; line-height: 16px; }

  .card--back-right .contact__name { left: 327px; top: 80px; }
  .card--back-right .contact__rule { left: 327px; top: 103px; width: 157px; }
  .card--back-right .contact__title { left: 316px; top: 110px; }
  .card--back-right .contact__line, .card--back-right .contact__office { right: 32px; text-align: right; }
  .card--back-right .contact__address { right: 40px; text-align: right; top: 250px; }

  .card--back-left .contact__name { left: 18px; top: 53px; }
  .card--back-left .contact__title { left: 18px; top: 82px; }
  .card--back-left .contact__rule { left: 18px; top: 106px; width: 149px; }
  .card--back-left .contact__line { left: 18px; }

  .address-band { position: absolute; left: 0; bottom: 0; width: 100%; height: 45px; background: var(--navy); }
  .address-band__text { position: absolute; left: 191px; top: 16px; color: var(--white); font-size: 9.5px; font-weight: 400; }
</style>
</head>
<body>

  <section class="card card--front-dark">
    <svg class="card__shape" viewBox="0 0 507 290" preserveAspectRatio="none" aria-hidden="true">
      <path d="M0 0 H212 Q90 45 0 116 Z" fill="var(--white)"/>
      <path d="M128 290 Q300 250 507 250 V290 Z" fill="var(--white)"/>
    </svg>
    <div class="brand__mark"></div>
    <div class="brand__name">HARROWFIELD</div>
    <div class="brand__sub">PROPERTY PARTNERS</div>
    <div class="brand__web">WWW.HRWPP-EXAMPLE.COM</div>
  </section>

  <section class="card card--back-right">
    <div class="photo" role="img" aria-label="Lighthouse casting a beam of light against a stormy sky"></div>
    <div class="mini-brand">
      <span class="mini-brand__mark"></span>
      <span class="mini-brand__name">HARROWFIELD<br>PROPERTY PARTNERS</span>
    </div>
    <div class="contact__name">Daniel R. Okafor</div>
    <div class="contact__rule"></div>
    <div class="contact__title">DIRECTOR OF OPERATIONS</div>
    <div class="contact__line" style="top:142px">(555) 010-7182</div>
    <div class="contact__line" style="top:166px">(555) 010-7182</div>
    <div class="contact__line contact__email" style="top:190px">d.okafor@hrwpp-example.com</div>
    <div class="contact__office" style="top:228px">USA Office</div>
    <div class="contact__address">48 Linden Crest Ave, Suite 840<br>Marlow Bay, FL 30100</div>
  </section>

  <section class="card card--front-light">
    <svg class="card__shape" viewBox="0 0 507 290" preserveAspectRatio="none" aria-hidden="true">
      <path d="M0 0 H240 Q95 40 0 115 Z" fill="var(--navy)"/>
      <path d="M78 290 Q280 246 507 242 V290 Z" fill="var(--navy)"/>
    </svg>
    <div class="brand__mark"></div>
    <div class="brand__name">HARROWFIELD</div>
    <div class="brand__sub">PROPERTY PARTNERS</div>
    <div class="brand__web">WWW.HRWPP-EXAMPLE.COM</div>
  </section>

  <section class="card card--back-left">
    <div class="photo" role="img" aria-label="Lighthouse casting a beam of light against a stormy sky"></div>
    <div class="contact__name">Daniel R. Okafor</div>
    <div class="contact__title">DIRECTOR OF OPERATIONS</div>
    <div class="contact__rule"></div>
    <div class="contact__line" style="top:127px">(555) 010-7182</div>
    <div class="contact__line" style="top:155px">(555) 010-7182</div>
    <div class="contact__line contact__email" style="top:183px">d.okafor@hrwpp-example.com</div>
    <div class="address-band">
      <div class="address-band__text">48 Linden Crest Ave, Suite 840, Marlow Bay, FL 30100</div>
    </div>
    <div class="mini-brand">
      <span class="mini-brand__mark"></span>
      <span class="mini-brand__name">HARROWFIELD<br>PROPERTY PARTNERS</span>
    </div>
  </section>

</body>
</html>
```